Modern HomePage Design for Church

We are looking for a modern homepage design using the sections we put together in the template. The colors we want are blue, black, grey, and white. We do not want use the colors in the logo. Please modify the logo color to match the website color scheme.

Target Market(s)

Church

Industry/Entity Type

Church

Number of Pages Required

1 page

Colors
0293ce
ffffff
474747
9d9d9d

```html
<!DOCTYPE html>
<html lang="en">
<head>
<meta charset="utf-8">
<title>Wellspring Grace Community Church — Home</title>
<link href="https://fonts.googleapis.com/css2?family=Lato:wght@300;400;700&family=Cormorant+SC:wght@400;500;600&family=Yellowtail&family=Kalam:wght@300&display=swap" rel="stylesheet">
<style>
:root{
  --blue:#0293ce;
  --white:#ffffff;
  --charcoal:#474747;
  --grey:#808080;
  --silver:#9d9d9d;
  --nav:#333333;
  --ink:#222222;
}
*{box-sizing:border-box;margin:0;padding:0}
html,body{width:1200px;height:1200px;overflow:hidden;background:var(--white)}
body{position:relative;font-family:'Lato',sans-serif;color:var(--white)}
.page{position:absolute;left:222px;top:0;width:839px;height:1500px;transform:scale(.8);transform-origin:0 0;overflow:hidden}
.abs{position:absolute}
.sc{font-family:'Cormorant SC',serif;font-weight:500}

/* nav */
.topnav{left:0;top:0;width:839px;height:28px;background:var(--nav)}
.topnav ul{list-style:none;position:absolute;left:198px;top:10px;display:flex;gap:20px;font-size:5.5px;letter-spacing:.3px;color:#cfcfcf}
.topnav li.active{color:var(--blue)}
.give{left:599px;top:3px;width:48px;height:22px;background:var(--blue);font-size:5px;display:flex;align-items:center;justify-content:center}

/* hero */
.hero{left:0;top:28px;width:839px;height:307px;background:radial-gradient(circle at 560px 80px,#ffcf6a 0,#f08a1e 40px,#a3460e 110px,#3a1a10 220px,#0b0b12 380px)}
.brand{left:198px;top:22px;width:64px;text-align:center;font-size:10px;letter-spacing:.5px;color:var(--blue)}
.brand small{display:block;font-size:3.6px;color:var(--white);letter-spacing:.2px}
.pill{top:12px;height:14px;background:#3b3b3b;border-radius:2px;font-size:4.6px;display:flex;align-items:center;justify-content:center}
.hero h1{left:24px;top:68px;font-size:31px;font-weight:500;letter-spacing:.5px}
.hero .script{left:150px;top:102px;font-family:'Yellowtail',cursive;font-size:62px}
.learn{left:198px;top:208px;width:118px;height:37px;background:rgba(140,140,140,.75);font-size:12px;letter-spacing:.6px;display:flex;align-items:center;justify-content:center}

/* band */
.band{left:0;top:335px;width:839px;height:31px;background:var(--blue)}
.band p{position:absolute;left:123px;top:11px;font-size:6.3px;letter-spacing:.2px}
.visitor{left:572px;top:7px;width:71px;height:16px;background:var(--charcoal);font-size:6.5px;display:flex;align-items:center;justify-content:center}

/* welcome */
.welcome{left:0;top:366px;width:593px;height:239px;background:var(--grey);padding:31px 33px}
.welcome h2{font-size:9px;font-weight:400;letter-spacing:.3px}
.welcome p{font-size:5.6px;line-height:13px;color:#e2e2e2;margin-top:0}
.welcome .lead{margin-bottom:26px}
.welcome .body{margin-bottom:20px;width:480px}
.portrait{left:595px;top:366px;width:244px;height:239px;background:linear-gradient(160deg,#f4f1ee 0,#c9b8a8 45%,#3b2a30 100%)}

/* meeting */
.meeting{left:0;top:605px;width:839px;height:130px;background:var(--charcoal)}
.meeting h3{left:33px;top:32px;font-size:18px;font-weight:600;letter-spacing:.6px}
.meeting .date{left:33px;top:55px;font-size:10.5px}
.meeting .note{left:33px;top:73px;width:200px;font-family:'Cormorant SC',serif;font-size:8px;line-height:8px;text-transform:none;font-variant:normal}
.count{left:354px;top:14px;width:110px}
.count .row{display:flex;align-items:center;height:27px;font-size:5px}
.count .lab{width:40px;font-family:'Cormorant SC',serif;font-size:6px}
.count .num{width:42px;text-align:center;font-size:18px;font-weight:300;border-bottom:1px solid #8a8a8a;margin:0 6px}
.count .arr{font-size:6px}
.meeting .side{left:612px;top:22px;width:210px;text-align:center;font-size:8.3px;line-height:8.3px}
.btn-white{background:var(--white);color:var(--ink);font-family:'Cormorant SC',serif;font-size:8px;display:flex;align-items:center;justify-content:center}
.btn-outline{border:1px solid var(--charcoal);background:var(--white);color:var(--charcoal);font-family:'Cormorant SC',serif;font-size:8px;display:flex;align-items:center;justify-content:center}
.btn-dark{background:var(--charcoal);border:1px solid var(--white);color:var(--white);font-family:'Cormorant SC',serif;font-size:8px;display:flex;align-items:center;justify-content:center}

/* features */
.features{left:0;top:735px;width:839px;height:243px;background:var(--white);color:var(--ink)}
.feature{position:absolute;top:24px;width:180px;text-align:center}
.feature svg{display:block;margin:0 auto;height:42px}
.feature h4{font-family:'Cormorant SC',serif;font-weight:500;font-size:15px;letter-spacing:.6px;margin-top:12px}
.feature p{font-family:'Cormorant SC',serif;font-size:9.5px;line-height:21.5px;margin-top:10px}
.feature .btn-outline{width:72px;height:17px;margin:20px auto 0}

/* ministries */
.tile{position:absolute}
.tag{position:absolute;background:var(--blue);font-family:'Cormorant SC',serif;font-size:10px;padding:4px 6px;white-space:nowrap}
.involved{left:510px;top:978px;width:329px;height:260px;background:var(--grey);text-align:center}
.involved h2,.blogs h2,.pray h2{font-family:'Cormorant SC',serif;font-weight:400;font-size:23px;letter-spacing:1px}
.involved p,.blogs p{font-family:'Cormorant SC',serif;font-size:9px;line-height:9.6px;width:280px;margin:24px auto 0}

/* bottom */
.blogs{left:0;top:1238px;width:324px;height:262px;background:var(--grey);text-align:center}
.divider{left:324px;top:1238px;width:2px;height:262px;background:var(--charcoal)}
.pray{left:326px;top:1238px;width:513px;height:262px;background:var(--blue);text-align:center}
.pray p{font-family:'Kalam',cursive;font-weight:300;font-size:14px;line-height:17px;width:420px;margin:22px auto 0}
</style>
</head>
<body>
<main class="page">

  <nav class="abs topnav">
    <ul>
      <li class="active">HOME</li><li>TEAM</li><li>FEATURES</li><li>EVENTS</li><li>SERMONS</li><li>CONTACTS</li><li>BLOG</li>
    </ul>
    <div class="abs give">GIVE ONLINE</div>
  </nav>

  <header class="abs hero" role="img" aria-label="Silhouette of a kneeling person before a cross at sunset">
    <div class="abs brand">WELLSPRING<small>GRACE COMMUNITY CHURCH</small></div>
    <div class="abs pill" style="left:497px;width:71px">SUNDAY WORSHIP 10:15</div>
    <div class="abs pill" style="left:573px;width:74px">SUNDAY SCHOOL 09H00</div>
    <h1 class="abs sc">Reaching And Resotring Through</h1>
    <div class="abs script">Revelation!</div>
    <div class="abs learn">LEARN MORE &gt;&gt;</div>
  </header>

  <section class="abs band">
    <p>LOREM IPSUM DOLOR SIT AMET, CONSECTETUER ADIPISCING ELIT, SED DIAM NONUMMY NIBH EUISMOD TINCIDUNT UT</p>
    <div class="abs visitor">VISITOR INFO</div>
  </section>

  <section class="abs welcome">
    <h2>WELCOME TO WELLSPRING GRACE COMMUNITY CHURCH</h2>
    <p class="lead">Lorem ipsum dolor sit amet, consectetuer adipiscing elit, sed</p>
    <p class="body">Lorem ipsum dolor sit amet, consectetuer adipiscing elit, sed diam nonummy nibh euismod tincidunt ut laoreet dolore magna aliquam erat volutpat. Ut wisi enim ad minim veniam, quis nostrud exerci tation ullamcorper suscipit lobortis nisl ut aliquip ex ea commodo consequat. Duis autem</p>
    <p class="body">Lorem ipsum dolor sit amet, consectetuer adipiscing elit, sed diam nonummy nibh euismod tincidunt ut laoreet dolore magna aliquam erat volutpat. Ut wisi enim ad minim veniam, quis nostrud exerci tation ullamcorper suscipit lobortis nisl ut aliquip ex ea commodo consequat. Duis autem vel eum iriure dolor in hendrerit in vulputate velit esse molestie consequat, vel illum dolore eu feugiat nulla facilisis at vero eros et ac-</p>
  </section>
  <div class="abs portrait" role="img" aria-label="Portrait of the senior pastor and his wife"></div>

  <section class="abs meeting">
    <h3 class="abs sc">Church Leaders Meeting</h3>
    <div class="abs date">Month 00 , 2019 00:00pm</div>
    <p class="abs note">Lorem ipsum dolor sit amet, consectetuer adipiscing elit, sed diam nonummy nibh euismod tincidunt ut</p>
    <div class="abs count">
      <div class="row"><span class="lab">Days</span><span class="arr">▾</span><span class="num">00</span><span class="arr">▴</span></div>
      <div class="row"><span class="lab">Hours</span><span class="arr">▾</span><span class="num">00</span><span class="arr">▴</span></div>
      <div class="row"><span class="lab">Minutes</span><span class="arr">▾</span><span class="num">00</span><span class="arr">▴</span></div>
      <div class="row"><span class="lab">Seconds</span><span class="arr">▾</span><span class="num">00</span><span class="arr">▴</span></div>
    </div>
    <p class="abs side sc">Lorem ipsum dolor sit amet, consectetuer adipiscing elit, sed diam nonummy nibh euismod tincidunt ut laoreet dolore magna aliquam erat volutpat. Ut wisi enim ad minim veniam, quis nostrud exerci tation ullamcorper suscipit lobortis nisl ut aliquip ex ea commodo consequat. Duis autem vel eum iriure</p>
    <div class="abs btn-white" style="left:681px;top:93px;width:72px;height:16px">Read more</div>
  </section>

  <section class="abs features">
    <div class="feature" style="left:36px">
      <svg viewBox="0 0 40 42" aria-hidden="true"><g fill="var(--blue)"><rect x="17" y="2" width="6" height="28"/><rect x="10" y="9" width="20" height="5"/><rect x="6" y="30" width="28" height="5"/><rect x="2" y="37" width="36" height="5"/></g></svg>
      <h4>What We Believe</h4>
      <p>Lorem ipsum dolor sit amet,<br>consectetuer adipiscing elit, sed<br>diam nonummy nibh euismod tin-</p>
      <div class="btn-outline">Read more</div>
    </div>
    <div class="feature" style="left:232px">
      <svg viewBox="0 0 40 42" aria-hidden="true"><path d="M20 2a10 10 0 0 0-10 10c0 8 10 18 10 18s10-10 10-18A10 10 0 0 0 20 2z" fill="var(--blue)"/><circle cx="20" cy="12" r="4" fill="#fff"/><path d="M4 36c8 0 10-4 16-4s8 4 16 2" stroke="var(--blue)" stroke-width="3" fill="none"/></svg>
      <h4>Services &amp; Location</h4>
      <p>Lorem ipsum dolor sit amet,<br>consectetuer adipiscing elit, sed<br>diam nonummy nibh euismod tin-</p>
      <div class="btn-outline">Read more</div>
    </div>
    <div class="feature" style="left:428px">
      <svg viewBox="0 0 56 42" aria-hidden="true"><rect x="2" y="4" width="38" height="34" rx="3" fill="none" stroke="var(--blue)" stroke-width="3"/><path d="M40 15l12-7v26l-12-7z" fill="none" stroke="var(--blue)" stroke-width="3"/><path d="M16 13l12 8-12 8z" fill="none" stroke="var(--blue)" stroke-width="3"/></svg>
      <h4>Watch Live</h4>
      <p>Lorem ipsum dolor sit amet,<br>consectetuer adipiscing elit, sed<br>diam nonummy nibh euismod tin-</p>
      <div class="btn-outline">Read more</div>
    </div>
    <div class="feature" style="left:624px">
      <svg viewBox="0 0 48 42" aria-hidden="true"><path d="M30 8c3-5 11-3 10 3-1 5-10 11-10 11s-9-6-10-11c-1-6 7-8 10-3z" fill="var(--blue)"/><path d="M2 26h10l8 4h12l-4 5H16" stroke="var(--blue)" stroke-width="4" fill="none"/></svg>
      <h4>Giving</h4>
      <p>Lorem ipsum dolor sit amet,<br>consectetuer adipiscing elit, sed<br>diam nonummy nibh euismod tin-</p>
      <div class="btn-outline">Read more</div>
    </div>
  </section>

  <section>
    <div class="tile" style="left:0;top:978px;width:269px;height:135px;background:linear-gradient(135deg,#b7c96a,#7d8f4e 60%,#c9c2b5)" role="img" aria-label="Seniors ministry group outdoors"><span class="tag" style="left:83px;top:97px">Seniors Ministry</span></div>
    <div class="tile" style="left:269px;top:978px;width:241px;height:135px;background:linear-gradient(135deg,#9c8a6e,#c79a6a 50%,#6b7f8f)" role="img" aria-label="Kids ministry children together"><span class="tag" style="left:82px;top:99px">Kids Ministry</span></div>
    <div class="tile" style="left:0;top:1113px;width:133px;height:125px;background:linear-gradient(135deg,#7d8a5e,#c7a27a 60%,#8d6c4f)" role="img" aria-label="Teens ministry group"><span class="tag" style="left:25px;top:97px">Teens Ministry</span></div>
    <div class="tile" style="left:133px;top:1113px;width:187px;height:125px;background:linear-gradient(180deg,#8f8f8f,#bdb6ad 55%,#7a4d2f)" role="img" aria-label="Hands folded over an open bible"><span class="tag" style="left:51px;top:97px">Bible Study</span></div>
    <div class="tile" style="left:320px;top:1113px;width:190px;height:125px;background:linear-gradient(135deg,#5f8a3e,#c99a72 55%,#6b9f47)" role="img" aria-label="Outreach ministry children"><span class="tag" style="left:52px;top:98px;font-size:8.5px">Outreach Ministry</span></div>
  </section>

  <section class="abs involved">
    <h2 style="margin-top:52px">Get Involved</h2>
    <p>Lorem ipsum dolor sit amet, consectetuer adipiscing elit, sed diam nonummy nibh euismod tincidunt ut laoreet dolore magna aliquam erat volutpat. Ut wisi enim ad minim veniam, quis nostrud exerci tation ullamcorper suscipit lobortis nisl ut aliquip ex ea commodo consequat. Duis autem vel</p>
    <div class="abs btn-dark" style="left:128px;top:180px;width:72px;height:17px">Read more</div>
  </section>

  <section class="abs blogs">
    <h2 style="margin-top:50px">Our Blogs</h2>
    <p>Lorem ipsum dolor sit amet, consectetuer adipiscing elit, sed diam nonummy nibh euismod tincidunt ut laoreet dolore magna aliquam erat volutpat. Ut wisi enim ad minim veniam, quis nostrud exerci tation ullamcorper suscipit lobortis nisl ut aliquip ex ea commodo consequat. Duis autem vel</p>
    <div class="abs btn-dark" style="left:132px;top:180px;width:72px;height:17px">Read more</div>
  </section>
  <div class="abs divider"></div>
  <section class="abs pray">
    <h2 style="margin-top:36px">Pray without Ceasing</h2>
    <p>Lorem ipsum dolor sit amet, consectetuer adipiscing elit, sed diam nonummy nibh euismod tincidunt ut laoreet dolore magna aliquam erat volutpat. Ut wisi enim ad minim veniam, quis nostrud exerci</p>
    <div class="abs btn-white" style="left:496px;top:174px;width:71px;height:16px;left:220px">Read more</div>
  </section>

</main>
</body>
</html>
```